business card for Cedar Grove Faith Assembly
Cedar Grove Faith Assembly of Eighth-hour Believers
Simple
Reginald Waldon
Pastor
4817 Orchard Ln. Harborview, ME 32417
CedarGroveFaithAssembly@quillpost.net
www.cedargrovefaithassembly.net
Business card should have our full name "Cedar Grove Faith Assembly of Eighth-hour Believers" and should utilize our logo fonts and colors.

```html
<!DOCTYPE html>
<html lang="en">
<head>
<meta charset="utf-8">
<title>Cedar Grove Faith Assembly — Business Card</title>
<link rel="stylesheet" href="https://fonts.googleapis.com/css2?family=Lato:wght@400;700;900&display=swap">
<style>
  :root {
    --page-bg: #e9e9e7;
    --card-white: #ffffff;
    --card-black: #1b1b1b;
    --card-black-soft: #232323;
    --brand-green: #2f9a3a;
    --brand-blue: #2aa7e0;
    --ink: #4a4a4a;
    --ink-soft: #7a7a7a;
  }
  * { box-sizing: border-box; margin: 0; padding: 0; }
  html, body {
    width: 1200px; height: 914px; overflow: hidden;
    background: var(--page-bg);
    font-family: "Lato", Arial, sans-serif;
  }
  .sheet {
    width: 1200px; height: 914px;
    display: flex; flex-direction: column; align-items: center; justify-content: center;
    gap: 34px;
  }
  .card {
    position: relative;
    width: 700px; height: 400px;
    border-radius: 14px;
    overflow: hidden;
    box-shadow: 0 6px 18px rgba(0,0,0,0.18);
  }

  /* Back side */
  .card-back {
    background: radial-gradient(ellipse at 60% 50%, var(--card-black-soft), var(--card-black) 70%);
  }
  .back-mark {
    position: absolute; left: 440px; top: 178px;
    display: flex; align-items: center; gap: 8px;
  }
  .back-mark .dot {
    width: 12px; height: 12px; border-radius: 50%;
    background: var(--brand-green);
  }
  .back-mark .name {
    font-weight: 700; font-size: 15px; color: var(--brand-green);
  }

  /* Front side */
  .card-front { background: var(--card-white); }
  .brand {
    position: absolute; left: 52px; top: 206px; width: 270px;
  }
  .brand-name {
    font-weight: 900; font-size: 26px; line-height: 1.1;
    color: var(--brand-green);
  }
  .brand-sub {
    margin-top: 8px;
    font-size: 13px; color: var(--ink-soft); letter-spacing: 0.3px;
  }
  .divider {
    position: absolute; left: 350px; top: 110px;
    width: 1.5px; height: 190px; background: var(--brand-green);
  }
  .contact {
    position: absolute; left: 372px; top: 104px; width: 310px;
    color: var(--ink);
  }
  .contact .person {
    font-weight: 700; font-size: 21px; color: var(--brand-green);
  }
  .contact .role {
    font-size: 13px; color: var(--ink-soft); margin-top: 2px;
  }
  .contact .address {
    font-size: 13px; line-height: 1.45; margin-top: 14px;
  }
  .contact ul { list-style: none; margin-top: 8px; }
  .contact li {
    display: flex; align-items: center; gap: 8px;
    font-size: 13px; line-height: 1.7; white-space: nowrap;
  }
  .contact li svg { width: 12px; height: 12px; flex: none; }
  .edge-bands {
    position: absolute; left: 0; bottom: 0; width: 700px; height: 40px;
  }
</style>
</head>
<body>
  <main class="sheet">
    <section class="card card-back" aria-label="Card back">
      <div class="back-mark">
        <span class="dot"></span>
        <span class="name">Cedar Grove Faith Assembly</span>
      </div>
    </section>

    <section class="card card-front" aria-label="Card front">
      <div class="brand">
        <div class="brand-name">Cedar Grove Faith Assembly</div>
        <div class="brand-sub">of Eighth-hour Believers</div>
      </div>

      <div class="divider"></div>

      <div class="contact">
        <div class="person">Reginald Waldon</div>
        <div class="role">Pastor</div>
        <div class="address">4817 Orchard Ln. Harborview,<br>ME 32417</div>
        <ul>
          <li>
            <svg viewBox="0 0 12 12" aria-hidden="true"><path d="M2.5 1h2l1 2.5-1.3 1a6 6 0 0 0 3.3 3.3l1-1.3L11 7.5v2a1 1 0 0 1-1 1A9 9 0 0 1 1.5 2a1 1 0 0 1 1-1z" fill="var(--brand-green)"/></svg>
            207-555-0186
          </li>
          <li>
            <svg viewBox="0 0 12 12" aria-hidden="true"><rect x="1" y="2.5" width="10" height="7" rx="1" fill="var(--brand-green)"/><path d="M1.5 3l4.5 3.5L10.5 3" stroke="#fff" stroke-width="0.9" fill="none"/></svg>
            CedarGroveFaithAssembly@quillpost.net
          </li>
          <li>
            <svg viewBox="0 0 12 12" aria-hidden="true"><circle cx="6" cy="6" r="4.8" fill="none" stroke="var(--brand-green)" stroke-width="1.2"/><path d="M1.2 6h9.6M6 1.2c-2.4 2.6-2.4 7 0 9.6M6 1.2c2.4 2.6 2.4 7 0 9.6" stroke="var(--brand-green)" stroke-width="0.9" fill="none"/></svg>
            www.cedargrovefaithassembly.net
          </li>
        </ul>
      </div>

      <svg class="edge-bands" viewBox="0 0 700 40" aria-hidden="true">
        <polygon points="0,30 470,30 450,40 0,40" fill="var(--brand-blue)"/>
        <polygon points="470,30 700,22 700,40 450,40" fill="var(--brand-green)"/>
      </svg>
    </section>
  </main>
</body>
</html>
```